Website for criminal defense attorney

Need a website that informs reader of my 26 years of practice, wins, practice areas (federal and capital cases, serious felonies, custody battles, etc), allows for payments (quidly app, remitro, dashu, kwiva, cards), etc. Client have referred to me as "The Iron Warden" "The Anvil" "Vanquisher". I do tend to use The Iron Warden motto and always play to win. Based in Atlanta but travel to other states. Color preferences are black and old gold, masonic themes and images (hidden), Rho Sigma Eta fraternity themes or images (likewise subtle or hidden), Spartan and warrior themes. Want strong, but not arrogant, Not about my ego, but about my ability to deliver. Have included business card, but not married to it and want to begin a brand of high end representation for remainder of my career.

```html
<!DOCTYPE html>
<html lang="en">
<head>
<meta charset="utf-8">
<title>Elliot R. Banks, LLC — Attorney at Law</title>
<link rel="stylesheet" href="https://fonts.googleapis.com/css2?family=Tinos&family=Nunito:wght@400;600;700&display=swap">
<style>
:root{
  --gold:#f4a948;
  --dark:#262626;
  --slate:#4a4b4d;
  --black:#141414;
  --field:#5b5b5b;
  --field-line:#8a8a8a;
  --white:#ffffff;
  --serif:"Tinos", "Times New Roman", serif;
  --sans:"Nunito", Arial, sans-serif;
}
*{margin:0;padding:0;box-sizing:border-box}
html,body{width:1200px;height:3224px;overflow:hidden}
body{position:relative;background:var(--dark);font-family:var(--sans);color:var(--white)}
.abs{position:absolute}

/* hero */
.hero{left:0;top:0;width:1200px;height:720px;
  background:linear-gradient(180deg,#3d5a86 0%,#7b8ea8 30%,#b9bec5 55%,#8a8d92 80%,#5f6266 100%)}
.brand-mark{left:119px;top:44px;font-family:var(--serif);font-size:26px;color:var(--gold);letter-spacing:1px}
.nav{right:142px;top:50px;display:flex;gap:44px;font-size:16px;font-weight:600}
.nav a{color:var(--white);text-decoration:none;position:relative}
.nav a.active{color:var(--gold)}
.nav a.active::after{content:"";position:absolute;left:0;right:0;bottom:-8px;height:2px;background:var(--gold)}
.hero-title{left:0;width:1200px;top:268px;text-align:center;font-family:var(--serif);font-size:55px;letter-spacing:1px;text-shadow:0 2px 6px rgba(0,0,0,.35)}
.hero-sub{left:0;width:1200px;top:342px;text-align:center;font-family:var(--serif);font-size:37px;text-shadow:0 2px 6px rgba(0,0,0,.35)}
.slide-arrow{top:291px;width:60px;height:60px}
.edge{left:0;width:1200px}

/* about */
.about-photo{left:182px;top:796px;width:374px;height:374px;border-radius:50%;
  background:radial-gradient(circle at 50% 45%,#b7998a 0%,#8a6e68 45%,#4d3f40 100%)}
.about-ring{left:155px;top:792px}
.section-heading{font-family:var(--serif);font-size:32px;color:var(--gold);letter-spacing:.5px}
.heading-rule{height:2px;background:var(--gold);width:119px}
.about-heading{left:598px;top:792px}
.about-rule{left:598px;top:841px}
.about-copy{left:598px;top:856px;width:465px;font-size:15.2px;line-height:24px;font-weight:600}
.about-copy p+p{margin-top:6px}
.btn{background:var(--gold);color:#262626;font-weight:700;font-size:15px;letter-spacing:1.5px;
  display:flex;align-items:center;justify-content:center;border-radius:4px}
.about-btn{left:599px;top:1122px;width:216px;height:49px}

/* practice */
.practice{left:0;top:1330px;width:1200px;height:850px;
  background:linear-gradient(180deg,#505154 0%,#4a4b4e 50%,#434447 100%)}
.practice-heading{left:0;width:1200px;top:1372px;text-align:center}
.practice-rule{left:541px;top:1421px}
.card{width:384px;height:299px;border-radius:8px;overflow:hidden;box-shadow:0 4px 12px rgba(0,0,0,.35)}
.card-label{position:absolute;left:0;right:0;bottom:0;height:110px;
  background:linear-gradient(180deg,rgba(20,20,20,0) 0%,rgba(20,20,20,.85) 100%);
  display:flex;align-items:flex-end;justify-content:center;padding-bottom:10px;
  font-family:var(--serif);font-size:30px;color:var(--gold);letter-spacing:.5px}
.card-federal{left:203px;top:1460px;background:linear-gradient(135deg,#b6c8d6,#6f8da6 50%,#3d5870)}
.card-capital{left:613px;top:1460px;background:linear-gradient(135deg,#e7e6e1,#9aa1a8 50%,#3e4557)}
.card-felonies{left:203px;top:1793px;background:linear-gradient(135deg,#eef0ec,#b8bdb0 50%,#4d4a44)}
.card-custody{left:613px;top:1793px;background:linear-gradient(135deg,#f1efea,#c9c5be 50%,#5a6f8d)}

/* contact */
.contact-heading{left:0;width:1200px;top:2257px;text-align:center}
.contact-rule{left:541px;top:2306px}
.contact-intro{left:0;width:1200px;top:2321px;text-align:center;font-size:17px;line-height:23px;font-weight:600;letter-spacing:.3px}
.field{background:var(--field);border:1px solid var(--field-line);display:flex;align-items:center;
  padding-left:14px;gap:12px;font-size:12.5px;font-weight:600;color:#e4e4e4}
.field-name{left:346px;top:2379px;width:507px;height:44px}
.field-email{left:346px;top:2433px;width:244px;height:44px}
.field-phone{left:608px;top:2433px;width:245px;height:44px}
.field-message{left:346px;top:2488px;width:507px;height:158px;align-items:flex-start;padding-top:14px}
.submit-btn{left:492px;top:2661px;width:215px;height:47px}

/* footer */
.footer{left:0;top:2890px;width:1200px;height:334px;background:var(--black)}
.footer-brand{left:229px;top:2950px;font-family:var(--serif);font-size:40px;line-height:48px;color:var(--gold)}
.footer-col h4{font-size:19px;font-weight:700;letter-spacing:.3px}
.footer-col .rule{width:44px;height:2px;background:var(--gold);margin:10px 0 14px}
.footer-col ul{list-style:none;font-size:12px;font-weight:600;line-height:24px}
.col-quick{left:464px;top:2932px}
.col-links{left:663px;top:2932px}
.col-contact{left:832px;top:2932px}
.contact-list{list-style:none;font-size:12px;font-weight:600}
.contact-list li{display:flex;gap:12px;align-items:flex-start;margin-bottom:13px;line-height:19px}
.contact-list svg{flex:none;margin-top:2px}
.footer-divider{left:111px;top:3150px;width:977px;height:1px;background:#5a5a5a}
.copyright{left:111px;top:3176px;font-size:14px;font-weight:600}
.payments{left:735px;top:3176px;display:flex;gap:18px;align-items:center;font-size:14px;font-weight:700;color:var(--white)}
.payments span{display:flex;align-items:center;gap:6px}
.payments i{display:inline-block;width:9px;height:9px;background:var(--gold)}
.to-top{left:1110px;top:3124px;width:44px;height:44px;border-radius:50%;background:var(--gold);display:flex;align-items:center;justify-content:center}
.chat-tag{left:1128px;top:3176px;font-size:14px;font-weight:700}
</style>
</head>
<body>

<!-- hero -->
<div class="abs hero" role="img" aria-label="Low-angle photograph of a columned courthouse facade with a seated marble statue against a blue sky"></div>
<div class="abs brand-mark">E. R. BANKS</div>
<nav class="abs nav">
  <a class="active" href="#">Home</a><a href="#">About</a><a href="#">Services</a><a href="#">News</a><a href="#">Contact</a>
</nav>
<h1 class="abs hero-title">ELLIOT R. BANKS, LLC</h1>
<div class="abs hero-sub">Attorney at Law</div>
<svg class="abs slide-arrow" style="left:23px" viewBox="0 0 60 60"><circle cx="30" cy="30" r="28" fill="none" stroke="#fff" stroke-width="2"/><path d="M38 30H22M28 24l-6 6 6 6" fill="none" stroke="#fff" stroke-width="2" stroke-linecap="round" stroke-linejoin="round"/></svg>
<svg class="abs slide-arrow" style="left:1116px" viewBox="0 0 60 60"><circle cx="30" cy="30" r="28" fill="none" stroke="#fff" stroke-width="2"/><path d="M22 30h16M32 24l6 6-6 6" fill="none" stroke="#fff" stroke-width="2" stroke-linecap="round" stroke-linejoin="round"/></svg>
<svg class="abs edge" style="top:630px" width="1200" height="92" viewBox="0 0 1200 92">
  <polygon points="0,14 600,74 1200,14 1200,92 0,92" fill="var(--gold)"/>
  <polygon points="0,24 600,84 1200,24 1200,92 0,92" fill="var(--dark)"/>
</svg>

<!-- about -->
<svg class="abs about-ring" width="220" height="382" viewBox="0 0 220 382">
  <path d="M218 4 A187 187 0 0 0 218 378" fill="none" stroke="var(--gold)" stroke-width="7"/>
</svg>
<div class="abs about-photo" role="img" aria-label="Illustration of a Spartan warrior in a red cape standing between stone arches"></div>
<h2 class="abs section-heading about-heading">ABOUT ELLIOT R. BANKS</h2>
<div class="abs heading-rule about-rule"></div>
<div class="abs about-copy">
  <p>Consectetur adipiscing elit, sed do eiusmod tempor incididunt ut labore et dolore magna aliqua. Ut enim ad minim veniam, quis nostrud exercitation ullamco laboris nisi ut aliquip ex ea commodo consequat. Duis aute irure dolor in reprehenderit in voluptate velit esse cillum dolore eu fugiat nulla pariatur. Excepteur sint occaecat cupidatat non proident, sunt in culpa qui officia deserunt mollit anim id est laboru</p>
  <p>Ut enim ad minim veniam, quis nostrud exercitation ullamco laboris nisi ut aliquip ex ea commodo consequat. Duis aute irure dolor in reprehenderit in voluptate velit esse.</p>
</div>
<a class="abs btn about-btn">LEARN MORE</a>

<!-- practice areas -->
<div class="abs practice" role="img" aria-label="Muted background photograph of rocky terrain"></div>
<svg class="abs edge" style="top:1250px" width="1200" height="82" viewBox="0 0 1200 82">
  <polygon points="0,66 600,8 1200,66 1200,82 0,82" fill="var(--gold)"/>
  <polygon points="0,76 600,18 1200,76 1200,82 0,82" fill="var(--slate)"/>
</svg>
<h2 class="abs section-heading practice-heading">PRACTICE AREAS</h2>
<div class="abs heading-rule practice-rule"></div>
<div class="abs card card-federal" role="img" aria-label="Photograph of financial network graphics with dollar symbols over a glass office"><div class="card-label">FEDERAL</div></div>
<div class="abs card card-capital" role="img" aria-label="Photograph of a lawyer consulting with a client at a desk"><div class="card-label">CAPITAL CASES</div></div>
<div class="abs card card-felonies" role="img" aria-label="Photograph of a woman working at a laptop in a bright office"><div class="card-label">SERIOUS FELONIES</div></div>
<div class="abs card card-custody" role="img" aria-label="Photograph of a father embracing his young daughter at home"><div class="card-label">CUSTODY BATTLES</div></div>

<!-- contact -->
<h2 class="abs section-heading contact-heading">CONTACT US</h2>
<div class="abs heading-rule contact-rule"></div>
<p class="abs contact-intro">Dolor sit amet, consectetur adipiscing elit, sed do<br>eiusmod tempor incididunt.</p>
<div class="abs field field-name">
  <svg width="14" height="14" viewBox="0 0 14 14"><circle cx="7" cy="4" r="3.2" fill="var(--gold)"/><path d="M1 14c0-4 2.7-6 6-6s6 2 6 6z" fill="var(--gold)"/></svg>Full Name *</div>
<div class="abs field field-email">
  <svg width="16" height="12" viewBox="0 0 16 12"><rect x=".5" y=".5" width="15" height="11" fill="none" stroke="var(--gold)"/><path d="M.5 .5 8 7l7.5-6.5" fill="none" stroke="var(--gold)"/></svg>Email *</div>
<div class="abs field field-phone">
  <svg width="14" height="14" viewBox="0 0 14 14"><path d="M3 0l3 3-2 2c1 2 3 4 5 5l2-2 3 3-2 3C6 14 0 8 0 3z" fill="var(--gold)"/></svg>Phone number *</div>
<div class="abs field field-message">
  <svg width="14" height="14" viewBox="0 0 14 14"><path d="M1 1l12 12" stroke="var(--gold)" stroke-width="2"/></svg>Enter Your Message&nbsp; *</div>
<a class="abs btn submit-btn">SUBMIT</a>

<!-- footer -->
<div class="abs footer"></div>
<svg class="abs edge" style="top:2822px" width="1200" height="82" viewBox="0 0 1200 82">
  <polygon points="0,66 600,10 1200,66 1200,82 0,82" fill="var(--gold)"/>
  <polygon points="0,76 600,20 1200,76 1200,82 0,82" fill="var(--black)"/>
</svg>
<div class="abs footer-brand">ELLIOT<br>R. BANKS</div>
<div class="abs footer-col col-quick">
  <h4>QUICK LINKS</h4><div class="rule"></div>
  <ul><li>HOME</li><li>ABOUT</li><li>SERVICES</li><li>NEWS</li><li>CONTACT</li></ul>
</div>
<div class="abs footer-col col-links">
  <h4>LINKS</h4><div class="rule"></div>
  <ul><li>COPYRIGHT</li><li>LEGAL</li><li>PRIVACY</li><li>ACCESSIBILITY</li><li>SITEMAP</li></ul>
</div>
<div class="abs footer-col col-contact">
  <h4>CONTACT US</h4><div class="rule"></div>
  <ul class="contact-list">
    <li><svg width="14" height="17" viewBox="0 0 14 17"><path d="M7 0a7 7 0 0 0-7 7c0 5 7 10 7 10s7-5 7-10a7 7 0 0 0-7-7z" fill="var(--gold)"/><circle cx="7" cy="7" r="2.5" fill="var(--black)"/></svg><span>2200, Harbor boulevard suite 300-B<br>atlanta, georgia 30301</span></li>
    <li><svg width="16" height="12" viewBox="0 0 16 12"><rect x=".5" y=".5" width="15" height="11" fill="none" stroke="var(--gold)"/><path d="M.5 .5 8 7l7.5-6.5" fill="none" stroke="var(--gold)"/></svg><span>attorneyelliotbanks@mailbox.com</span></li>
    <li><svg width="15" height="15" viewBox="0 0 14 14"><path d="M3 0l3 3-2 2c1 2 3 4 5 5l2-2 3 3-2 3C6 14 0 8 0 3z" fill="var(--gold)"/></svg><span>555-010-4412</span></li>
    <li><svg width="16" height="15" viewBox="0 0 16 15"><rect x="4" y="0" width="8" height="4" fill="var(--gold)"/><rect x="0" y="5" width="16" height="6" rx="1" fill="var(--gold)"/><rect x="4" y="9" width="8" height="6" fill="var(--gold)" stroke="var(--black)"/></svg><span>555-010-4490</span></li>
  </ul>
</div>
<div class="abs footer-divider"></div>
<div class="abs copyright">©2021. All rights reserved.</div>
<div class="abs payments">
  <span><i></i>Remitro</span><span>Quidly App</span><span>Dashu</span><span>Kwiva</span>
</div>
<div class="abs to-top"><svg width="14" height="9" viewBox="0 0 14 9"><path d="M1 8l6-6 6 6" fill="none" stroke="#262626" stroke-width="2"/></svg></div>
<div class="abs chat-tag">C44</div>

</body>
</html>
```